Business Card Design

We are a state licensed general contractor on the south east coast of Florida. We are a remodeling and home repairs business that have been in business for 14 years. Since we are located on the coast and our business name is Ridgeline Builders of Pine Hollow, Inc, we would like a "Ridgeline" themed design that would appeal to more affluent customers. I would like to see light blue colors with waves incorporated into the design. I would also like the design to communicate a modern, confident, responsible company character.

Industry/Entity Type

Contractor

Contact Information for Business Card

Tim Wexler 555-274-9183

```html
<!DOCTYPE html>
<html lang="en">
<head>
<meta charset="utf-8">
<title>Ridgeline Builders – Business Card</title>
<link href="https://fonts.googleapis.com/css2?family=Open+Sans:wght@400;600;700&display=swap" rel="stylesheet">
<style>
  :root {
    --page-bg: #e4e5e7;
    --card-white: #ffffff;
    --soft-grey: #eceef1;
    --wave-blue: #35b3df;
    --brand-blue: #1f5fa6;
    --charcoal: #3a3b3e;
    --charcoal-deep: #232427;
    --text-light: #f2f2f2;
    --text-muted: #b9bcc1;
  }
  * { margin: 0; padding: 0; box-sizing: border-box; }
  html, body {
    width: 1200px; height: 818px; overflow: hidden;
    background: var(--page-bg);
    font-family: "Open Sans", Arial, sans-serif;
  }
  .card {
    position: absolute; left: 180px; top: 169px;
    width: 840px; height: 480px;
    background: var(--card-white);
    box-shadow: 0 6px 24px rgba(0,0,0,.18);
    overflow: hidden;
  }
  .card-art { position: absolute; inset: 0; }
  .brand {
    position: absolute; left: 60px; top: 98px;
    display: flex; align-items: center; gap: 16px;
  }
  .brand-dot {
    width: 36px; height: 36px; border-radius: 50%;
    background: var(--brand-blue);
  }
  .brand-name {
    font-size: 56px; font-weight: 600; color: var(--brand-blue);
    line-height: 1;
  }
  .person {
    position: absolute; right: 40px; top: 92px; text-align: right;
    color: var(--text-light);
  }
  .person-name { font-size: 30px; font-weight: 700; line-height: 1.1; }
  .person-role { font-size: 15px; color: var(--text-muted); }
  .address {
    position: absolute; right: 40px; top: 190px;
    font-size: 18px; color: var(--text-light);
  }
  .contacts {
    position: absolute; left: 60px; top: 348px;
    list-style: none; font-size: 19px; line-height: 28px;
    color: var(--text-light);
  }
  .contact-label { color: var(--wave-blue); font-weight: 600; margin-right: 6px; }
</style>
</head>
<body>
  <div class="card">
    <svg class="card-art" viewBox="0 0 840 480" width="840" height="480" aria-hidden="true">
      <defs>
        <linearGradient id="charcoalFade" x1="0" y1="0" x2="1" y2="1">
          <stop offset="0" stop-color="var(--charcoal)"/>
          <stop offset="1" stop-color="var(--charcoal-deep)"/>
        </linearGradient>
      </defs>
      <path class="wave-soft" fill="var(--soft-grey)"
            d="M560,0 C480,110 300,200 0,255 L0,292 C360,230 555,130 635,0 Z"/>
      <path class="wave-blue" fill="var(--wave-blue)"
            d="M635,0 C555,130 360,230 0,292 L0,320 C400,250 600,140 680,0 Z"/>
      <path class="panel-dark" fill="url(#charcoalFade)"
            d="M680,0 C600,140 400,250 0,320 L0,480 L840,480 L840,0 Z"/>
    </svg>

    <div class="brand">
      <span class="brand-dot"></span>
      <span class="brand-name">Ridgeline</span>
    </div>

    <div class="person">
      <div class="person-name">Tim Wexler</div>
      <div class="person-role">owner</div>
    </div>

    <div class="address">4120 Harlow Circle, Pine Hollow, FL 33901</div>

    <ul class="contacts">
      <li><span class="contact-label">Cell</span>555-274-9183</li>
      <li><span class="contact-label">Office</span>555-318-6042</li>
      <li><span class="contact-label">Fax</span>555-318-7759</li>
      <li>ridgeline.tw@example.com</li>
    </ul>
  </div>
</body>
</html>
```